i need to make design for the our cover of three products:
Lemon scented Trash Bags
Strawberry scented Trash Bags
Lavender scented Trash Bags
all are with the same information i.e. the size, company name , number of bags etc the only difference is the scent
good examples are attached.
its also required that our brand is visible place in the design our brand "ovrolo" logo is attached as well
the cover design size is 10H*33W cm

Target Market(s)

commodity

Industry/Entity Type

plastic

Font styles to use
Serif
Sans Serif

```html
<!DOCTYPE html>
<html lang="en">
<head>
<meta charset="utf-8">
<title>ovrolo scented drawstring refuse sacks – pack covers</title>
<link href="https://fonts.googleapis.com/css2?family=Oswald:wght@500;600&family=Roboto:wght@400;700&display=swap" rel="stylesheet">
<style>
  :root{
    --green:#1b8a45;
    --green-deep:#127036;
    --gold-light:#f0d9a4;
    --gold-dark:#a9783a;
    --paper:#f4f4f2;
    --ink-soft:#6d6d6d;
    --white:#ffffff;
  }
  html,body{margin:0;padding:0;width:1200px;height:1200px;overflow:hidden;background:var(--white);}
  .sheet{position:relative;width:1200px;height:1200px;}
  .pack-cover{position:absolute;left:80px;width:1040px;height:315px;display:block;}
  .pack-cover--lemon{top:60px;--tone:#f7d008;--tone-deep:#e9b600;--tint:#efe6b4;}
  .pack-cover--lavender{top:442px;--tone:#a452a9;--tone-deep:#8a3d95;--tint:#c9a4c8;}
  .pack-cover--strawberry{top:824px;--tone:#ef1d1f;--tone-deep:#d2100f;--tint:#f1c3c8;}
  .tone{fill:var(--tone);}
  .tint{fill:var(--tint);}
  .title{font-family:"Oswald",sans-serif;font-weight:600;font-size:29px;fill:var(--green);}
  .spec{font-family:"Roboto",sans-serif;font-size:8.5px;fill:var(--ink-soft);letter-spacing:.2px;}
  .brand{font-family:"Roboto",sans-serif;font-weight:400;font-size:94px;fill:var(--white);}
  .badge-text{font-family:"Oswald",sans-serif;font-weight:600;fill:var(--white);text-anchor:middle;}
  .badge-scent{font-size:36px;}
  .badge-scent--long{font-size:24px;}
  .badge-word{font-size:31px;}
  .badge-note{font-size:15px;font-weight:500;}
  .ribbon{fill:var(--green-deep);}
  .ribbon-text{font-family:"Oswald",sans-serif;font-weight:600;font-size:26px;fill:var(--white);text-anchor:middle;}
  .fit-line{font-family:"Roboto",sans-serif;font-size:14px;fill:var(--green);}
  .fit-line--bold{font-weight:700;}
  .can-icon{fill:none;stroke:var(--green);stroke-width:1.6;}
  .can-number{font-family:"Oswald",sans-serif;font-weight:600;font-size:20px;fill:var(--green);text-anchor:middle;}
  .can-label{font-family:"Roboto",sans-serif;font-size:6px;fill:var(--green);text-anchor:middle;}
</style>
</head>
<body>
<main class="sheet">

  <!-- Lemon -->
  <svg class="pack-cover pack-cover--lemon" viewBox="0 0 1040 315" xmlns="http://www.w3.org/2000/svg">
    <defs>
      <linearGradient id="lemon-paper" x1="0" y1="0" x2="0" y2="1"><stop offset="0" stop-color="#f6f6f4"/><stop offset="1" stop-color="#ecebe6"/></linearGradient>
      <linearGradient id="lemon-scene" x1="0" y1="0" x2="1" y2="1"><stop offset="0" style="stop-color:var(--tone)"/><stop offset="1" style="stop-color:var(--tone-deep)"/></linearGradient>
      <linearGradient id="lemon-gold" x1="0" y1="0" x2="1" y2="1"><stop offset="0" style="stop-color:var(--gold-light)"/><stop offset=".5" style="stop-color:var(--gold-dark)"/><stop offset="1" style="stop-color:var(--gold-light)"/></linearGradient>
    </defs>
    <rect class="paper" width="1040" height="315" fill="url(#lemon-paper)"/>
    <rect class="tint" y="212" width="520" height="103"/>
    <rect class="tone" y="104" width="560" height="108"/>
    <polygon points="628,0 646,0 381,315 363,315" fill="url(#lemon-gold)"/>
    <polygon role="img" aria-label="Photo of a white drawstring bag with green ties among lemons and lemon leaves" points="642,0 1040,0 1040,315 377,315" fill="url(#lemon-scene)"/>
    <text class="title" x="14" y="42">DRAWSTRING REFUSE SACKS</text>
    <text class="spec" x="15" y="55">65x70 | LEMON SCENTED | YELLOW | 60 LT | 10 PCS</text>
    <text class="brand" x="46" y="190">ovrolo</text>
    <g class="can-badge">
      <path class="can-icon" d="M12,247 H60 L55,302 H17 Z"/>
      <text class="can-label" x="36" y="255">FITS</text>
      <text class="can-number" x="36" y="277">15</text>
      <text class="can-label" x="36" y="287">GALLON</text>
      <text class="can-label" x="36" y="296">CAN</text>
    </g>
    <text class="fit-line" x="66" y="262">GRIPS-THE CAN</text>
    <text class="fit-line fit-line--bold" x="66" y="280">TALL KITCHEN</text>
    <text class="fit-line" x="66" y="298">DRAWSRING BAGS</text>
    <path d="M520,42 C570,42 608,52 626,62 L622,140 C615,200 572,236 520,256 C468,236 425,200 418,140 L414,62 C432,52 470,42 520,42Z" fill="url(#lemon-gold)"/>
    <path class="tone" transform="translate(520,148) scale(.84) translate(-520,-148)" d="M520,42 C570,42 608,52 626,62 L622,140 C615,200 572,236 520,256 C468,236 425,200 418,140 L414,62 C432,52 470,42 520,42Z"/>
    <text class="badge-text badge-scent" x="520" y="120">LEMON</text>
    <text class="badge-text badge-word" x="520" y="154">SCENTED</text>
    <text class="badge-text badge-note" x="520" y="177">ODOR CONTROL</text>
    <polygon class="ribbon" points="446,262 1040,262 1040,302 412,302"/>
    <text class="ribbon-text" x="730" y="293">10 MEDIUM PACKS | 15 GALLON DRAWSTRING</text>
  </svg>

  <!-- Lavender -->
  <svg class="pack-cover pack-cover--lavender" viewBox="0 0 1040 315" xmlns="http://www.w3.org/2000/svg">
    <defs>
      <linearGradient id="lav-paper" x1="0" y1="0" x2="0" y2="1"><stop offset="0" stop-color="#f6f6f4"/><stop offset="1" stop-color="#ecebe6"/></linearGradient>
      <linearGradient id="lav-scene" x1="0" y1="0" x2="1" y2="1"><stop offset="0" style="stop-color:var(--tone)"/><stop offset="1" style="stop-color:var(--tone-deep)"/></linearGradient>
      <linearGradient id="lav-gold" x1="0" y1="0" x2="1" y2="1"><stop offset="0" style="stop-color:var(--gold-light)"/><stop offset=".5" style="stop-color:var(--gold-dark)"/><stop offset="1" style="stop-color:var(--gold-light)"/></linearGradient>
    </defs>
    <rect class="paper" width="1040" height="315" fill="url(#lav-paper)"/>
    <rect class="tint" y="212" width="520" height="103"/>
    <rect class="tone" y="104" width="560" height="108"/>
    <polygon points="628,0 646,0 381,315 363,315" fill="url(#lav-gold)"/>
    <polygon role="img" aria-label="Photo of a white drawstring bag with green ties among lavender sprigs" points="642,0 1040,0 1040,315 377,315" fill="url(#lav-scene)"/>
    <text class="title" x="14" y="42">DRAWSTRING REFUSE SACKS</text>
    <text class="spec" x="15" y="55">65x70 | LEMON SCENTED | YELLOW | 60 LT | 10 PCS</text>
    <text class="brand" x="46" y="190">ovrolo</text>
    <g class="can-badge">
      <path class="can-icon" d="M12,247 H60 L55,302 H17 Z"/>
      <text class="can-label" x="36" y="255">FITS</text>
      <text class="can-number" x="36" y="277">15</text>
      <text class="can-label" x="36" y="287">GALLON</text>
      <text class="can-label" x="36" y="296">CAN</text>
    </g>
    <text class="fit-line" x="66" y="262">GRIPS-THE CAN</text>
    <text class="fit-line fit-line--bold" x="66" y="280">TALL KITCHEN</text>
    <text class="fit-line" x="66" y="298">DRAWSRING BAGS</text>
    <path d="M520,42 C570,42 608,52 626,62 L622,140 C615,200 572,236 520,256 C468,236 425,200 418,140 L414,62 C432,52 470,42 520,42Z" fill="url(#lav-gold)"/>
    <path class="tone" transform="translate(520,148) scale(.84) translate(-520,-148)" d="M520,42 C570,42 608,52 626,62 L622,140 C615,200 572,236 520,256 C468,236 425,200 418,140 L414,62 C432,52 470,42 520,42Z"/>
    <text class="badge-text badge-word" x="520" y="118">LAVENDER</text>
    <text class="badge-text badge-word" x="520" y="152">SCENTED</text>
    <text class="badge-text badge-note" x="520" y="176">ODOR CONTROL</text>
    <polygon class="ribbon" points="446,262 1040,262 1040,302 412,302"/>
    <text class="ribbon-text" x="730" y="293">10 MEDIUM PACKS | 15 GALLON DRAWSTRING</text>
  </svg>

  <!-- Strawberry -->
  <svg class="pack-cover pack-cover--strawberry" viewBox="0 0 1040 315" xmlns="http://www.w3.org/2000/svg">
    <defs>
      <linearGradient id="straw-paper" x1="0" y1="0" x2="0" y2="1"><stop offset="0" stop-color="#f6f6f4"/><stop offset="1" stop-color="#ecebe6"/></linearGradient>
      <linearGradient id="straw-scene" x1="0" y1="0" x2="1" y2="1"><stop offset="0" style="stop-color:var(--tone)"/><stop offset="1" style="stop-color:var(--tone-deep)"/></linearGradient>
      <linearGradient id="straw-gold" x1="0" y1="0" x2="1" y2="1"><stop offset="0" style="stop-color:var(--gold-light)"/><stop offset=".5" style="stop-color:var(--gold-dark)"/><stop offset="1" style="stop-color:var(--gold-light)"/></linearGradient>
    </defs>
    <rect class="paper" width="1040" height="315" fill="url(#straw-paper)"/>
    <rect class="tint" y="212" width="520" height="103"/>
    <rect class="tone" y="104" width="560" height="108"/>
    <polygon points="628,0 646,0 381,315 363,315" fill="url(#straw-gold)"/>
    <polygon role="img" aria-label="Photo of a white drawstring bag with green ties among fresh strawberries" points="642,0 1040,0 1040,315 377,315" fill="url(#straw-scene)"/>
    <text class="title" x="14" y="42">DRAWSTRING REFUSE SACKS</text>
    <text class="spec" x="15" y="55">65x70 | LEMON SCENTED | YELLOW | 60 LT | 10 PCS</text>
    <text class="brand" x="46" y="190">ovrolo</text>
    <g class="can-badge">
      <path class="can-icon" d="M12,247 H60 L55,302 H17 Z"/>
      <text class="can-label" x="36" y="255">FITS</text>
      <text class="can-number" x="36" y="277">15</text>
      <text class="can-label" x="36" y="287">GALLON</text>
      <text class="can-label" x="36" y="296">CAN</text>
    </g>
    <text class="fit-line" x="66" y="262">GRIPS-THE CAN</text>
    <text class="fit-line fit-line--bold" x="66" y="280">TALL KITCHEN</text>
    <text class="fit-line" x="66" y="298">DRAWSRING BAGS</text>
    <path d="M520,42 C570,42 608,52 626,62 L622,140 C615,200 572,236 520,256 C468,236 425,200 418,140 L414,62 C432,52 470,42 520,42Z" fill="url(#straw-gold)"/>
    <path class="tone" transform="translate(520,148) scale(.84) translate(-520,-148)" d="M520,42 C570,42 608,52 626,62 L622,140 C615,200 572,236 520,256 C468,236 425,200 418,140 L414,62 C432,52 470,42 520,42Z"/>
    <text class="badge-text badge-scent--long" x="520" y="114">STRAWBERRY</text>
    <text class="badge-text badge-word" x="520" y="150">SCENTED</text>
    <text class="badge-text badge-note" x="520" y="175">ODOR CONTROL</text>
    <polygon class="ribbon" points="446,262 1040,262 1040,302 412,302"/>
    <text class="ribbon-text" x="730" y="293">10 MEDIUM PACKS | 15 GALLON DRAWSTRING</text>
  </svg>

</main>
</body>
</html>
```